Med Spa business card design with logo

Need a logo design and business card for our new company Velora Skinworks Med Spa. We are a medical office that deals with high end clients. We offer them skin care products which include NERVAX, lip augmentation, and various laser for the skin. I king of like the logo attached, maybe something along those lines but also open to any logo concept.
Updates

Target Market(s)

Out target audience are male and females in the age range of 21-80 years of age

Industry/Entity Type

Medical

Contact Information for Business Card

woukd like front of card to have logo and business name VELORA SKINWORKS MEDSPA. Back of card employee name and phone number along with instagram logo and user name

Font styles to use
Serif
Sans Serif

Requirements
Must have
• prefer monochromatic look white, black, gold
Should not have
• not too colorful

```html
<!DOCTYPE html>
<html lang="en">
<head>
<meta charset="utf-8">
<title>Velora Skinworks Med Spa — Business Card</title>
<link rel="stylesheet" href="https://fonts.googleapis.com/css2?family=Lato:wght@700;900&family=Oswald:wght@500&family=Open+Sans:wght@400&display=swap">
<style>
  :root {
    --backdrop: #2b2b2d;
    --gold-light: #e2b95c;
    --gold-mid: #c89b3c;
    --gold-deep: #8c6428;
    --ink: #6a4818;
    --ink-soft: #7d5a26;
    --seal: #c9c9c9;
  }
  * { margin: 0; padding: 0; box-sizing: border-box; }
  html, body {
    width: 1200px; height: 1000px; overflow: hidden;
    background: var(--backdrop);
  }
  .stage {
    position: relative; width: 1200px; height: 1000px;
  }
  .card {
    position: absolute; left: 170px; width: 860px; height: 440px;
    background: linear-gradient(180deg,
      var(--gold-mid) 0%, var(--gold-deep) 16%, var(--gold-light) 34%,
      var(--gold-deep) 52%, var(--gold-light) 70%, var(--gold-deep) 86%, var(--gold-mid) 100%);
    box-shadow: 0 14px 30px rgba(0,0,0,.45);
  }
  .card--front { top: 40px; }
  .card--back { top: 520px; }

  .brand {
    position: absolute; inset: 0;
    display: flex; flex-direction: column; align-items: center; justify-content: center; gap: 26px;
  }
  .brand__seal {
    width: 84px; height: 84px; border-radius: 50%; background: var(--seal);
  }
  .brand__name {
    font-family: "Lato", sans-serif; font-weight: 900; font-size: 24px;
    letter-spacing: 3px; color: var(--ink);
  }

  .person {
    position: absolute; left: 150px; top: 150px; width: 250px; text-align: right;
  }
  .person__name {
    font-family: "Oswald", sans-serif; font-weight: 500; font-size: 44px;
    letter-spacing: 1px; color: var(--ink); line-height: 1.1;
  }
  .person__title {
    font-family: "Open Sans", sans-serif; font-size: 21px; letter-spacing: 1px;
    color: var(--ink-soft);
  }
  .divider {
    position: absolute; left: 430px; top: 120px; width: 2px; height: 140px; background: var(--ink-soft);
  }
  .contact {
    position: absolute; left: 460px; top: 115px;
    font-family: "Open Sans", sans-serif; font-size: 20px; color: var(--ink-soft); line-height: 1.3;
  }
  .contact__address { margin-bottom: 10px; }
  .contact__row { display: flex; align-items: center; gap: 14px; margin-top: 4px; }
  .contact__icon { width: 16px; height: 16px; fill: var(--ink-soft); flex: none; }
</style>
</head>
<body>
<main class="stage">
  <section class="card card--front">
    <div class="brand">
      <div class="brand__seal"></div>
      <div class="brand__name">VELORA SKINWORKS MEDSPA</div>
    </div>
  </section>

  <section class="card card--back">
    <div class="person">
      <div class="person__name">ADRIEN VALE</div>
      <div class="person__title">CEO &amp; FOUNDER</div>
    </div>
    <div class="divider"></div>
    <div class="contact">
      <div class="contact__address">Your Street Address,<br>Singapore, 1234</div>
      <div class="contact__row">
        <svg class="contact__icon" viewBox="0 0 16 16"><path d="M3 1l3 3-1.5 2a9 9 0 0 0 5.5 5.5L12 10l3 3-2 2C6 15 1 10 1 3z"/></svg>
        <span>+000 123 456 789</span>
      </div>
      <div class="contact__row">
        <svg class="contact__icon" viewBox="0 0 16 16"><path d="M1 3h14v10H1z M1 3l7 6 7-6" fill="none" stroke="currentColor" stroke-width="0"/><path d="M1 3h14L8 9z"/><path d="M1 5l7 6 7-6v8H1z"/></svg>
        <span>yourname@email.com</span>
      </div>
      <div class="contact__row">
        <svg class="contact__icon" viewBox="0 0 16 16"><circle cx="8" cy="8" r="7"/><path d="M1 8h14M8 1v14M3 4h10M3 12h10" stroke="#c89b3c" stroke-width="1" fill="none"/></svg>
        <span>www.websitename.com</span>
      </div>
    </div>
  </section>
</main>
</body>
</html>
```